I need some Graphic Design for a product label "Plume Nectar"

I need a product label designed for my new product.
"Plume Nectar"
I am wanting the label to have a CLEAR BACKING with BLACK WRITING.

It will need to say:

"Plume Nectar" -Bold but easy to read script

Raw Cashews
Vanilla Bean
Filtered Water

X Hand made X Raw X Pure

750ml

I have attached some examples of labels I like to get a idea of the style and font ideas
I would like the words "Plume Nectar" in a bold text so it stands out, the rest of the font I would like a more delicate script.
Any questions please contact me :)

```html
<!DOCTYPE html>
<html lang="en">
<head>
<meta charset="utf-8">
<title>Plume Nectar — Label</title>
<link rel="stylesheet" href="https://fonts.googleapis.com/css2?family=Comfortaa:wght@500&family=Oleo+Script:wght@700&family=Poiret+One&family=Ubuntu:wght@700&display=swap">
<style>
  :root {
    --label-bg: #ffffff;
    --ink: #111111;
    --badge-text: #ffffff;
  }
  html, body {
    margin: 0;
    padding: 0;
    overflow: hidden;
    background: var(--label-bg);
  }
  .label {
    position: relative;
    width: 1200px;
    height: 960px;
    background: var(--label-bg);
    color: var(--ink);
    overflow: hidden;
  }
  .label__name {
    position: absolute;
    top: 108px;
    left: 0;
    width: 100%;
    margin: 0;
    text-align: center;
    font-family: "Oleo Script", cursive;
    font-weight: 700;
    font-size: 104px;
    line-height: 1;
    letter-spacing: -1px;
  }
  .ingredients {
    position: absolute;
    top: 332px;
    left: 0;
    width: 100%;
    margin: 0;
    padding: 0;
    list-style: none;
    text-align: center;
    font-family: "Poiret One", sans-serif;
    font-size: 68px;
    line-height: 105px;
  }
  .tagline {
    position: absolute;
    top: 714px;
    left: 0;
    width: 100%;
    margin: 0;
    text-align: center;
    font-family: "Comfortaa", sans-serif;
    font-weight: 500;
    font-size: 32px;
    letter-spacing: 1px;
  }
  .volume {
    position: absolute;
    top: 836px;
    left: 547px;
    width: 106px;
    height: 44px;
    background: var(--ink);
    color: var(--badge-text);
    font-family: "Ubuntu", sans-serif;
    font-weight: 700;
    font-size: 29px;
    line-height: 44px;
    text-align: center;
    letter-spacing: -1px;
  }
</style>
</head>
<body>
  <main class="label">
    <h1 class="label__name">Plume Nectar</h1>
    <ul class="ingredients">
      <li>Raw Cashews</li>
      <li>Vanilla Bean</li>
      <li>Filtered Water</li>
    </ul>
    <p class="tagline">.x. Hand made .x. Raw .x. Pure .x.</p>
    <div class="volume">750ml</div>
  </main>
</body>
</html>
```